Visitenkarten für Goldankauf
Zielgruppe
wir sind fokussiert auf den Goldankauf
Aufgabenstellung
es soll elegant aber auch bisschen auffällig sein. aber nichts verspieltes
es heißt die Brennecks Wertecke
logo habe ich nicht

```html
<!DOCTYPE html>
<html lang="de">
<head>
<meta charset="utf-8">
<title>Brennecks Wertecke – Visitenkarten</title>
<link rel="stylesheet" href="https://fonts.googleapis.com/css2?family=Noto+Serif:wght@400;700&display=swap">
<style>
  :root {
    --gold: #debc7e;
    --black: #030303;
    --paper: #ffffff;
    --ground: #f3f3f3;
    --ink: #3c3c3c;
    --ink-dark: #111111;
  }
  * { margin: 0; padding: 0; box-sizing: border-box; }
  html, body { width: 1200px; height: 1056px; overflow: hidden; }
  body {
    position: relative;
    background: var(--ground);
    font-family: "Noto Serif", Georgia, serif;
  }
  .band { position: absolute; }
  .band--gold { left: 619px; top: 0; width: 581px; height: 65px; background: var(--gold); }
  .band--black { left: 0; top: 991px; width: 581px; height: 65px; background: var(--black); }

  .card {
    position: absolute;
    top: 370px;
    width: 484px;
    height: 313px;
    overflow: hidden;
    box-shadow: 2px 3px 4px rgba(0,0,0,.35);
  }
  .card--front { left: 98px; background: var(--black); }
  .card--back { left: 622px; background: var(--paper); }

  /* front */
  .front-rule {
    position: absolute; left: 125px; top: 42px;
    width: 1px; height: 231px; background: var(--paper);
  }
  .front-name {
    position: absolute; left: 136px; top: 38px;
    color: var(--gold);
    font-size: 24px; line-height: 28px; letter-spacing: .5px;
    text-transform: uppercase;
  }
  .front-tagline {
    position: absolute; left: 136px; top: 254px;
    color: var(--gold);
    font-size: 8px; line-height: 11px; letter-spacing: .6px;
  }

  /* back */
  .name-block {
    position: absolute; left: 0; top: 0;
    width: 258px; height: 58px; background: var(--gold);
  }
  .person-name {
    position: absolute; left: 40px; top: 28px;
    color: var(--paper); font-weight: 700; font-size: 23px; line-height: 28px;
    white-space: nowrap;
  }
  .person-role {
    position: absolute; left: 41px; top: 62px;
    color: var(--ink); font-size: 13px;
  }
  .contact {
    position: absolute; left: 258px; top: 114px;
    color: var(--ink); font-size: 10.5px; line-height: 18.2px;
  }
  .contact strong { font-weight: 700; }
  .contact .gap { height: 13.5px; }
  .back-name {
    position: absolute; left: 41px; top: 243px;
    color: var(--ink-dark);
    font-size: 16px; line-height: 19px; letter-spacing: .3px;
    text-transform: uppercase;
  }
  .web-bar {
    position: absolute; left: 283px; top: 253px;
    width: 201px; height: 25px; background: var(--gold);
    color: var(--paper); font-size: 10.5px; line-height: 25px;
    padding-left: 13px;
  }
  .web-icon { position: absolute; left: 246px; top: 247px; width: 37px; height: 37px; }
</style>
</head>
<body>
  <div class="band band--gold"></div>
  <div class="band band--black"></div>

  <section class="card card--front">
    <div class="front-rule"></div>
    <div class="front-name">Brennecks<br>Wertecke</div>
    <p class="front-tagline">Professionelle und faire Bewertung<br>Ihrer Schmuckstücke</p>
  </section>

  <section class="card card--back">
    <div class="name-block"></div>
    <h1 class="person-name">Tim Brenneck</h1>
    <p class="person-role">Inhaber</p>

    <div class="contact">
      <strong>Brennecks Wertecke</strong><br>
      Lindenweg 14<br>
      80469 München
      <div class="gap"></div>
      <strong>Fon</strong> 089 / 41207365<br>
      <strong>Mobil</strong> 0171 / 2853046<br>
      kontakt@wertecke-ankauf.de
    </div>

    <div class="back-name">Brennecks<br>Wertecke</div>

    <div class="web-bar">www.wertecke-ankauf.de</div>
    <svg class="web-icon" viewBox="0 0 37 37" aria-hidden="true">
      <circle cx="18.5" cy="18.5" r="18.5" fill="var(--gold)"/>
      <g fill="none" stroke="#fff" stroke-width="1.1">
        <circle cx="18.5" cy="18.5" r="11"/>
        <ellipse cx="18.5" cy="18.5" rx="5" ry="11"/>
        <line x1="18.5" y1="7.5" x2="18.5" y2="29.5"/>
        <line x1="7.5" y1="18.5" x2="29.5" y2="18.5"/>
        <path d="M9.5 12.5 H27.5 M9.5 24.5 H27.5"/>
      </g>
    </svg>
  </section>
</body>
</html>
```